Gutschein-Design für Versandhandel mit mehreren Webshops
Zielgruppe
Wir sind ein Versandhandel mit mehreren Webshops
Durch eine Paketbeigabe in Form von Gummibärchen in Pyramidenpackung möchten wir insbesondere unsere Webshops www.tafelhof.at und www.most-keltern.at bewerben
3 Seiten zur Verfügung
1 x Slogan 'Danke für den Kauf oder ähnlich'
1 x Rabattaktion für tafelhof.at
1 x Rabattaktion für most-keltern.at
Die Empfänger sind bereits Kunden ggf. von anderen Kanälen (kaufnetz etc)
Ziel ist es den Kunden direkt auf unsere Website zu bringen
Aufgabenstellung
die Logos der Websites tafelhof.at als auch most-keltern.at sowie ein Rabatt-Kupon-Code (gerne witzig oder kreativ) samt gültigkeit etc. müssen angeführt sein

```html
<!DOCTYPE html>
<html lang="de">
<head>
<meta charset="utf-8">
<title>Pyramiden-Gutschein – Faltvorlage</title>
<link rel="stylesheet" href="https://fonts.googleapis.com/css2?family=Open+Sans:wdth,wght@75..100,400..800&family=Permanent+Marker&family=Outfit:wght@600;700&display=swap">
<style>
  :root {
    --bg: #e1f7e8;
    --paper: #ffffff;
    --water-deep: #0b5d9e;
    --water-light: #2aa3db;
    --band-cool: #e6edf2;
    --gold: #d7a548;
    --beer: #f3b713;
    --beer-deep: #e59a0b;
    --foam: #f6eedb;
    --cream: #f7f0df;
    --brown: #5a3a25;
    --ink: #2a2117;
    --pill-ink: #222222;
    --gummy-red: #ef2f4f;
    --gummy-pink: #f45a9a;
    --gummy-orange: #ff7a2a;
    --gummy-yellow: #ffd23c;
    --mint: #9fdcc0;
    --mint-text: #8fd3b4;
  }
  * { margin: 0; padding: 0; box-sizing: border-box; }
  html, body { width: 1162px; height: 1200px; overflow: hidden; background: var(--bg); }
  .canvas { position: relative; width: 1162px; height: 1200px; }
  .dieline {
    position: absolute; left: 31px; top: 368px; width: 1100px; height: 465px;
    filter: drop-shadow(0 6px 10px rgba(60, 120, 90, 0.15));
  }
  .copy { font-family: "Open Sans", Arial, sans-serif; font-stretch: 80%; font-weight: 700; }
  .copy-white { fill: var(--paper); }
  .copy-dark { fill: var(--ink); }
  .code { font-family: "Open Sans", Arial, sans-serif; font-stretch: 85%; font-weight: 400; fill: var(--pill-ink); letter-spacing: 2px; }
  .brand { font-family: "Open Sans", Arial, sans-serif; font-stretch: 80%; font-weight: 800; }
  .brand-tafelhof { fill: var(--gold); }
  .brand-most { fill: var(--brown); }
  .slogan { font-family: "Permanent Marker", "Arial Black", sans-serif; fill: var(--paper); }
  .legal-note { font-family: "Outfit", Arial, sans-serif; font-weight: 700; fill: var(--mint-text); font-size: 22px; }
  .frame { fill: none; stroke: var(--paper); stroke-width: 6; stroke-linejoin: round; opacity: 0.9; }
  .hatch { stroke: var(--mint); stroke-width: 2; opacity: 0.55; }
</style>
</head>
<body>
<div class="canvas">
  <svg class="dieline" viewBox="150 1140 1610 680" xmlns="http://www.w3.org/2000/svg">
    <defs>
      <linearGradient id="water" x1="-300" y1="-354" x2="300" y2="177" gradientUnits="userSpaceOnUse">
        <stop offset="0" stop-color="var(--water-light)"/>
        <stop offset="0.5" stop-color="var(--water-deep)"/>
        <stop offset="1" stop-color="var(--water-light)"/>
      </linearGradient>
      <linearGradient id="gummy" x1="808" y1="1215" x2="808" y2="1750" gradientUnits="userSpaceOnUse">
        <stop offset="0" stop-color="var(--gummy-yellow)"/>
        <stop offset="0.35" stop-color="var(--gummy-orange)"/>
        <stop offset="0.7" stop-color="var(--gummy-red)"/>
        <stop offset="1" stop-color="var(--gummy-pink)"/>
      </linearGradient>
      <linearGradient id="beer" x1="200" y1="-300" x2="-100" y2="100" gradientUnits="userSpaceOnUse">
        <stop offset="0" stop-color="var(--foam)"/>
        <stop offset="0.25" stop-color="var(--foam)"/>
        <stop offset="0.4" stop-color="var(--beer)"/>
        <stop offset="1" stop-color="var(--beer-deep)"/>
      </linearGradient>
      <clipPath id="face-upright"><polygon points="0,-354 -306.5,177 306.5,177"/></clipPath>
      <clipPath id="face-legal"><polygon points="1423,1269 1161,1723 1688,1723"/></clipPath>
    </defs>

    <!-- glue flaps -->
    <g class="flaps" fill="var(--paper)">
      <rect x="195" y="1165" width="613" height="90" rx="50"/>
      <rect x="500" y="1710" width="615" height="90" rx="50"/>
      <polygon points="195,1215 500,1750 468,1752 172,1238" stroke="var(--paper)" stroke-width="40" stroke-linejoin="round"/>
    </g>

    <!-- face: tafelhof.at coupon (drawn upright, turned into place) -->
    <g class="face face-tafelhof" transform="translate(501 1393.3) rotate(60)">
      <g clip-path="url(#face-upright)">
        <rect x="-320" y="-360" width="640" height="540" fill="url(#water)" role="img" aria-label="Hintergrundfoto: bewegtes blaues Wasser"/>
        <rect class="brand-band" x="-320" y="73" width="640" height="110" fill="var(--band-cool)"/>
      </g>
      <polygon class="frame" points="0,-290 -201,58 201,58"/>
      <text class="copy copy-white" x="0" y="-130" font-size="26" text-anchor="middle">Jetzt</text>
      <text class="copy copy-white" x="0" y="-101" font-size="26" text-anchor="middle">Rabatt-Code</text>
      <text class="copy copy-white" x="0" y="-72" font-size="26" text-anchor="middle">einlösen!</text>
      <rect class="code-pill" x="-120" y="-58" width="240" height="78" rx="39" fill="var(--paper)"/>
      <text class="code" x="0" y="-7" font-size="34" text-anchor="middle">XXXXXXXX</text>
      <text class="copy copy-white" x="0" y="46" font-size="24" text-anchor="middle">Gültig bis 31.12.2022.</text>
      <text class="brand brand-tafelhof" x="0" y="146" font-size="54" text-anchor="middle">tafelhof.at</text>
    </g>

    <!-- face: thank-you slogan -->
    <g class="face face-slogan">
      <polygon points="808,1215 500,1750 1115,1750" fill="url(#gummy)" role="img" aria-label="Hintergrundfoto: bunte Gummibärchen in Rot, Orange, Gelb und Pink"/>
      <polygon class="frame" points="808,1286 562,1714 1054,1714"/>
      <text class="slogan" x="808" y="1478" font-size="46" text-anchor="middle" textLength="150" lengthAdjust="spacingAndGlyphs">Vielen</text>
      <text class="slogan" x="808" y="1565" font-size="86" text-anchor="middle" textLength="226" lengthAdjust="spacingAndGlyphs">Dank</text>
      <text class="slogan" x="808" y="1614" font-size="40" text-anchor="middle" textLength="78" lengthAdjust="spacingAndGlyphs">für</text>
      <text class="slogan" x="808" y="1684" font-size="44" text-anchor="middle" textLength="330" lengthAdjust="spacingAndGlyphs">Ihre Bestellung!</text>
    </g>

    <!-- face: most-keltern.at coupon (drawn upright, turned into place) -->
    <g class="face face-most" transform="translate(1115.3 1393.3) rotate(-60)">
      <g clip-path="url(#face-upright)">
        <rect x="-320" y="-360" width="640" height="540" fill="url(#beer)" role="img" aria-label="Hintergrundfoto: Bier mit Schaumkrone und Perlen"/>
        <rect class="brand-band" x="-320" y="73" width="640" height="110" fill="var(--cream)"/>
      </g>
      <polygon class="frame" points="0,-290 -201,58 201,58"/>
      <text class="copy copy-dark" x="0" y="-130" font-size="26" text-anchor="middle">Jetzt</text>
      <text class="copy copy-dark" x="0" y="-101" font-size="26" text-anchor="middle">Rabatt-Code</text>
      <text class="copy copy-dark" x="0" y="-72" font-size="26" text-anchor="middle">einlösen!</text>
      <rect class="code-pill" x="-120" y="-58" width="240" height="78" rx="39" fill="var(--paper)"/>
      <text class="code" x="0" y="-7" font-size="34" text-anchor="middle">XXXXXXXX</text>
      <text class="copy copy-dark" x="0" y="46" font-size="24" text-anchor="middle">Gültig bis 31.12.2022.</text>
      <text class="brand brand-most" x="0" y="146" font-size="52" text-anchor="middle">most-keltern.at</text>
    </g>

    <!-- face: reserved for legal info -->
    <g class="face face-legal">
      <polygon points="1423,1215 1115,1750 1735,1750" fill="var(--paper)"/>
      <g clip-path="url(#face-legal)">
        <line class="hatch" x1="1100" y1="1290" x2="1750" y2="1300"/>
        <line class="hatch" x1="1100" y1="1312" x2="1750" y2="1322"/>
        <line class="hatch" x1="1100" y1="1334" x2="1750" y2="1344"/>
        <line class="hatch" x1="1100" y1="1356" x2="1750" y2="1366"/>
        <line class="hatch" x1="1100" y1="1378" x2="1750" y2="1388"/>
        <line class="hatch" x1="1100" y1="1400" x2="1750" y2="1410"/>
        <line class="hatch" x1="1100" y1="1422" x2="1750" y2="1432"/>
        <line class="hatch" x1="1100" y1="1444" x2="1750" y2="1454"/>
        <line class="hatch" x1="1100" y1="1466" x2="1750" y2="1476"/>
        <line class="hatch" x1="1100" y1="1570" x2="1750" y2="1580"/>
        <line class="hatch" x1="1100" y1="1592" x2="1750" y2="1602"/>
        <line class="hatch" x1="1100" y1="1614" x2="1750" y2="1624"/>
        <line class="hatch" x1="1100" y1="1636" x2="1750" y2="1646"/>
        <line class="hatch" x1="1100" y1="1658" x2="1750" y2="1668"/>
        <line class="hatch" x1="1100" y1="1680" x2="1750" y2="1690"/>
        <line class="hatch" x1="1100" y1="1702" x2="1750" y2="1712"/>
      </g>
      <text class="legal-note" x="1428" y="1508" text-anchor="middle">reserviert</text>
      <text class="legal-note" x="1428" y="1534" text-anchor="middle">für</text>
      <text class="legal-note" x="1428" y="1560" text-anchor="middle">Pflichtangaben</text>
    </g>
  </svg>
</div>
</body>
</html>
```